NEW HIP COOL PROGRESSIVE FUN PPE BUSINESS IN NEED OF STANDOUT ADS

Design a banner ad that is cool, hip, and happening related to PPE. We have a healthcare business that is uber conservative and we have all the "proper" and dull ads to represent the seriousness of our true mission and passion. tidelumo.com is an e-commerce non-medical PPE business based in Hawaii. We are ready to share our brand with more people online. Help us create something fun and progressive. Get inspiration from our under construction e-commerce store....tidelumo.com
Updates

Low design quality

Target Market(s)

BUSINESSES IN NEED OF PPE OPENING UP, FAMILIES AND INDIVIDUALS IN NEED OF PPE, SCHOOLS IN NEED OF PPE.

Industry/Entity Type

Medical Supply

Font styles to use
Serif
Sans Serif

Requirements
Must have
• Add some hawaiian or local flair. Don't make it look so clinical. This is a site for consumers and businesses.

```html
<!DOCTYPE html>
<html lang="en">
<head>
<meta charset="utf-8">
<title>Tidelumo Banner Ad Designs</title>
<link rel="stylesheet" href="https://fonts.googleapis.com/css2?family=Montserrat:wght@400;500;600;800&family=Poppins:wght@400;700&family=Kalam:wght@400&display=swap">
<style>
  :root {
    --green-dark: #0b5e2a;
    --green-mid: #167a38;
    --green-text: #1e8a3a;
    --white: #ffffff;
    --button: #666666;
    --curve: #5f5f5f;
    --heading: #55626b;
    --body-text: #7d8b94;
    --sky-top: #bfe6f5;
    --sky-bottom: #9fd0e0;
  }
  * { box-sizing: border-box; margin: 0; padding: 0; }
  html, body { width: 1200px; height: 1150px; overflow: hidden; }
  body { font-family: "Montserrat", Arial, sans-serif; position: relative; }

  .backdrop {
    position: absolute; inset: 0;
    background: linear-gradient(180deg, var(--sky-top) 0%, #d6eef6 45%, #c3e3ea 70%, var(--sky-bottom) 100%);
  }

  .banner {
    position: absolute; background: var(--white); overflow: hidden;
    box-shadow: 4px 6px 10px rgba(0,0,0,0.25);
  }
  .banner--leaderboard { left: 117px; top: 84px; width: 988px; height: 122px; }
  .banner--rectangle { left: 567px; top: 244px; width: 456px; height: 380px; }
  .banner--skyscraper { left: 117px; top: 244px; width: 407px; height: 814px; }

  .green-panel { position: absolute; left: 0; top: 0; }

  .headline {
    position: absolute; color: var(--white); font-weight: 800;
    text-transform: uppercase; line-height: 0.95; letter-spacing: 0.5px;
  }
  .tagline {
    position: absolute; background: var(--white); color: #222;
    font-weight: 500; text-transform: uppercase; white-space: nowrap; text-align: center;
  }
  .ship-note {
    position: absolute; color: var(--white); font-family: "Kalam", cursive; line-height: 1.35;
  }
  .product {
    position: absolute; border-radius: 40px;
    background: radial-gradient(ellipse at 35% 55%, #9fd6e6 0%, #c9e8f0 40%, #eef5f7 70%, rgba(255,255,255,0) 100%);
  }
  .brand {
    position: absolute; color: var(--green-text); font-weight: 600; white-space: nowrap; z-index: 2;
  }
  .pitch { position: absolute; color: var(--green-text); font-weight: 400; z-index: 2; }
  .order-button {
    position: absolute; background: var(--button); color: var(--white);
    font-weight: 500; text-transform: uppercase; display: flex;
    align-items: center; justify-content: center; white-space: nowrap; z-index: 2;
  }

  /* leaderboard */
  .banner--leaderboard .headline { left: 24px; top: 16px; font-size: 31px; }
  .banner--leaderboard .tagline { left: 26px; top: 84px; width: 180px; height: 20px; font-size: 12px; line-height: 20px; }
  .banner--leaderboard .ship-note { left: 234px; top: 32px; font-size: 16px; }
  .banner--leaderboard .product { left: 392px; top: 6px; width: 118px; height: 110px; border-radius: 30px; }
  .banner--leaderboard .brand { left: 520px; top: 52px; font-size: 15px; }
  .banner--leaderboard .pitch { left: 645px; top: 34px; width: 172px; font-size: 13px; line-height: 1.4; }
  .banner--leaderboard .order-button { left: 830px; top: 42px; width: 136px; height: 37px; font-size: 14px; }

  /* rectangle */
  .banner--rectangle .headline { left: 16px; top: 20px; font-size: 34px; }
  .banner--rectangle .tagline { left: 20px; top: 95px; width: 181px; height: 20px; font-size: 12px; line-height: 20px; }
  .banner--rectangle .ship-note { left: 16px; top: 124px; font-size: 16px; }
  .banner--rectangle .product { left: 30px; top: 168px; width: 262px; height: 192px; }
  .banner--rectangle .brand { right: 18px; top: 42px; font-size: 22px; }
  .banner--rectangle .pitch { right: 20px; top: 142px; width: 130px; font-size: 17px; line-height: 1.4; text-align: right; }
  .banner--rectangle .order-button { left: 299px; top: 318px; width: 136px; height: 37px; font-size: 14px; }

  /* skyscraper */
  .banner--skyscraper .headline { left: 0; width: 100%; top: 54px; font-size: 56px; text-align: center; }
  .banner--skyscraper .tagline { left: 78px; top: 182px; width: 251px; height: 26px; font-size: 17px; line-height: 26px; }
  .banner--skyscraper .ship-note { left: 0; width: 100%; top: 228px; font-size: 22px; text-align: center; }
  .banner--skyscraper .product { left: 30px; top: 300px; width: 346px; height: 236px; }
  .banner--skyscraper .brand { left: 0; width: 100%; top: 582px; font-size: 27px; text-align: center; }
  .banner--skyscraper .pitch { left: 40px; width: 327px; top: 640px; font-size: 19px; line-height: 1.6; text-align: center; }
  .banner--skyscraper .order-button { left: 136px; top: 741px; width: 136px; height: 37px; font-size: 15px; }

  .showcase-copy { position: absolute; left: 583px; top: 726px; width: 560px; }
  .showcase-title { font-family: "Poppins", Arial, sans-serif; font-weight: 700; font-size: 46px; color: var(--heading); letter-spacing: 0.3px; }
  .showcase-text { font-family: "Poppins", Arial, sans-serif; font-size: 17px; line-height: 1.45; color: var(--body-text); margin-top: 22px; }
  .showcase-text + .showcase-text { margin-top: 24px; }
</style>
</head>
<body>
  <div class="backdrop" role="img" aria-label="Soft tropical beach scene with palm trees"></div>

  <section class="banner banner--leaderboard">
    <svg class="green-panel" width="440" height="122" viewBox="0 0 440 122" role="img" aria-label="Palm trees tinted green">
      <defs>
        <linearGradient id="greenLeader" x1="0" y1="0" x2="1" y2="1">
          <stop offset="0" stop-color="#0b5e2a"/><stop offset="1" stop-color="#1a8a3e"/>
        </linearGradient>
      </defs>
      <path d="M0 0 H380 Q392 61 374 122 H0 Z" fill="url(#greenLeader)"/>
      <path d="M380 0 Q392 61 374 122" fill="none" stroke="var(--curve)" stroke-width="7"/>
    </svg>
    <h2 class="headline">Safety<br>Supplies</h2>
    <div class="tagline">From Hawaii for Hawaii</div>
    <p class="ship-note">but we'll<br>ship to<br>anyone!</p>
    <div class="product" role="img" aria-label="Blue face mask and clear face shield"></div>
    <div class="brand">tidelumo.com</div>
    <p class="pitch">Hawaii-based, ships fast, local pick-up &amp; delivery available!</p>
    <div class="order-button">Order Now</div>
  </section>

  <section class="banner banner--skyscraper">
    <svg class="green-panel" width="407" height="380" viewBox="0 0 407 380" role="img" aria-label="Palm trees tinted green">
      <defs>
        <linearGradient id="greenSky" x1="0" y1="0" x2="0" y2="1">
          <stop offset="0" stop-color="#0b5e2a"/><stop offset="1" stop-color="#1a8a3e"/>
        </linearGradient>
      </defs>
      <path d="M0 0 H407 V348 Q200 320 0 366 Z" fill="url(#greenSky)"/>
      <path d="M407 348 Q200 320 0 366" fill="none" stroke="var(--curve)" stroke-width="6"/>
    </svg>
    <h2 class="headline">Safety<br>Supplies</h2>
    <div class="tagline">From Hawaii for Hawaii</div>
    <p class="ship-note">but we'll ship to<br>anyone!</p>
    <div class="product" role="img" aria-label="Blue face mask and clear face shield"></div>
    <div class="brand">tidelumo.com</div>
    <p class="pitch">Hawaii-based, ships fast, local pick-up &amp; delivery available!</p>
    <div class="order-button">Order Now</div>
  </section>

  <section class="banner banner--rectangle">
    <svg class="green-panel" width="260" height="380" viewBox="0 0 260 380" role="img" aria-label="Palm trees tinted green">
      <defs>
        <linearGradient id="greenRect" x1="0" y1="0" x2="1" y2="1">
          <stop offset="0" stop-color="#0b5e2a"/><stop offset="1" stop-color="#1a8a3e"/>
        </linearGradient>
      </defs>
      <path d="M0 0 H186 Q262 190 206 380 H0 Z" fill="url(#greenRect)"/>
      <path d="M186 0 Q262 190 206 380" fill="none" stroke="var(--curve)" stroke-width="7"/>
    </svg>
    <h2 class="headline">Safety<br>Supplies</h2>
    <div class="tagline">From Hawaii for Hawaii</div>
    <p class="ship-note">but we'll ship to<br>anyone!</p>
    <div class="product" role="img" aria-label="Blue face mask and clear face shield"></div>
    <div class="brand">tidelumo.com</div>
    <p class="pitch">Hawaii-based, ships fast, local pick-up &amp; delivery available!</p>
    <div class="order-button">Order Now</div>
  </section>

  <div class="showcase-copy">
    <h1 class="showcase-title">Banner Ad Designs</h1>
    <p class="showcase-text">Contrary to popular belief, Lorem Ipsum is not simply random text. It has roots in a piece of classical Latin literature from 45 BC, making it over 2000 years old.</p>
    <p class="showcase-text">Contrary to popular belief, Lorem Ipsum is not simply random text. It has roots in a piece of classical Latin literatur</p>
  </div>
</body>
</html>
```